All Natural Raw Honey & Goats Milk Body Wash Labels

We have launched a new product line of all natural Raw Honey & Goats Milk body wash with the business name being Dawn Meadow and the tag line Naturally . Their are currently three line items requiring three labels. Natural (Unscented), Japanese Honeysuckle and Caribbean.
It is a family orientated product that we want to promote as being all natural, healthy and trustworthy. It is an all Australian made product that uses our very own award winning raw honey
I can supply the file for the business name/logo upon request

Target Market(s)

Families

Industry/Entity Type

Bath & body

Requirements
Must have
• a Lux high end feel
Nice to have
• simple easy to read with minimal images
Should not have
• No cartoons

```html
<!DOCTYPE html>
<html lang="en">
<head>
<meta charset="utf-8">
<title>Dawn Meadow – Raw Honey &amp; Goats Milk Label</title>
<link href="https://fonts.googleapis.com/css2?family=Della+Respira&family=Dancing+Script:wght@700&family=Montserrat:wght@700&display=swap" rel="stylesheet">
<style>
  :root {
    --backdrop: #eceeef;
    --label: #ffffff;
    --ink: #111111;
    --honey: #e0922a;
    --honey-deep: #c4701b;
    --cup: #5a3323;
    --leaf: #4f9a2f;
  }
  * { margin: 0; padding: 0; box-sizing: border-box; }
  html, body {
    width: 1200px;
    height: 1200px;
    overflow: hidden;
    background: var(--backdrop);
  }
  .canvas {
    position: relative;
    width: 1200px;
    height: 1200px;
  }
  .label {
    position: absolute;
    left: 316px;
    top: 50px;
    width: 568px;
    height: 1100px;
    background: var(--label);
    box-shadow: 0 2px 10px rgba(0,0,0,0.06);
  }
  .label-frame {
    position: absolute;
    inset: 14px;
    border: 2px solid var(--ink);
  }
  .brand {
    position: absolute;
    top: 170px;
    left: 0;
    right: 0;
    display: flex;
    align-items: center;
    justify-content: center;
    gap: 14px;
  }
  .brand-dot {
    width: 22px;
    height: 22px;
    border-radius: 50%;
    background: var(--ink);
  }
  .brand-name {
    font-family: "Della Respira", serif;
    font-size: 54px;
    color: var(--ink);
    line-height: 1;
  }
  .ingredients-art {
    position: absolute;
    left: 60px;
    top: 394px;
    width: 460px;
    height: 322px;
    border-radius: 8px;
    background:
      radial-gradient(ellipse at 30% 65%, var(--honey) 0%, var(--honey-deep) 32%, transparent 55%),
      radial-gradient(ellipse at 56% 35%, var(--cup) 0%, #3e2217 28%, transparent 50%),
      radial-gradient(ellipse at 78% 72%, var(--leaf) 0%, #3d7a22 22%, transparent 42%),
      #fbf6ef;
  }
  .product-title {
    position: absolute;
    top: 742px;
    left: 0;
    right: 0;
    text-align: center;
    font-family: "Della Respira", serif;
    font-size: 62px;
    line-height: 74px;
    color: var(--ink);
  }
  .variant {
    position: absolute;
    top: 900px;
    left: 0;
    right: 0;
    text-align: center;
    font-family: "Dancing Script", cursive;
    font-weight: 700;
    font-size: 50px;
    color: var(--ink);
  }
  .volume {
    position: absolute;
    top: 990px;
    left: 0;
    right: 0;
    text-align: center;
    font-family: "Montserrat", sans-serif;
    font-weight: 700;
    font-size: 30px;
    letter-spacing: 1px;
    color: #222222;
  }
</style>
</head>
<body>
  <main class="canvas">
    <section class="label">
      <div class="label-frame"></div>
      <div class="brand">
        <span class="brand-dot"></span>
        <span class="brand-name">Dawn Meadow</span>
      </div>
      <div class="ingredients-art" role="img" aria-label="Honeycomb dripping raw honey beside a clay cup of goats milk and a sprig of fresh basil leaves"></div>
      <h1 class="product-title">Raw Honey &amp;<br>Goats Milk</h1>
      <p class="variant">Natural</p>
      <p class="volume">30ML</p>
    </section>
  </main>
</body>
</html>
```